Stationery Design
Letterhead, Envelope, Business Card, Email signature design
I need single sided standard sized Business Card [3.5" x 2"]
Myriad Pro
Professional
Corisse Pallant
Brand Manager
4127 Dunford Avenue
Burnaby, B.C. V3K 8T2
604-281-7734 ext. 120
corisse@brightfernco.ca
brightfernco.ca
We are a family-owned school photography company in Western Canada. We've just had a new logo and website designed and need some new stationery.
This is the .ai file we would like to use for the stationery design. Please refer to our website, brightfernco.ca, for more information about our brand.

```html
<!DOCTYPE html>
<html lang="en">
<head>
<meta charset="utf-8">
<title>Brightfern Co — Business Cards</title>
<link rel="stylesheet" href="https://fonts.googleapis.com/css2?family=Source+Sans+3:wght@400;600;700&display=swap">
<style>
  :root {
    --backdrop: #e4e6e8;
    --card-white: #ffffff;
    --card-silver: #eef0f1;
    --brand-blue: #2a9fc6;
    --ink: #4a4f55;
    --ink-soft: #6d737a;
    --on-blue: #ffffff;
  }
  * { margin: 0; padding: 0; box-sizing: border-box; }
  html, body { width: 1200px; height: 737px; overflow: hidden; }
  body {
    background: var(--backdrop);
    font-family: "Source Sans 3", sans-serif;
    color: var(--ink);
    position: relative;
  }
  .card {
    position: absolute;
    border-radius: 10px;
    box-shadow: 0 6px 18px rgba(0,0,0,0.22);
    overflow: hidden;
  }
  .card--front {
    left: 360px; top: 108px; width: 571px; height: 264px;
    background: linear-gradient(180deg, var(--card-white) 0%, var(--card-silver) 100%);
  }
  .card--back-light {
    left: 108px; top: 384px; width: 468px; height: 252px;
    background: linear-gradient(180deg, var(--card-white) 0%, var(--card-silver) 100%);
  }
  .card--back-blue {
    left: 595px; top: 384px; width: 473px; height: 252px;
    background: var(--brand-blue);
  }
  .brand-name {
    font-weight: 700;
    color: var(--brand-blue);
    letter-spacing: 0.5px;
    white-space: nowrap;
  }
  .card--front .brand-name {
    position: absolute; left: 26px; top: 28px;
    font-size: 38px; line-height: 1;
  }
  .contact-name {
    position: absolute; left: 30px; top: 96px;
    font-size: 18px; font-weight: 600; color: var(--brand-blue);
  }
  .contact-title {
    position: absolute; left: 30px; top: 116px;
    font-size: 15px; color: var(--ink);
  }
  .contact-address {
    position: absolute; left: 30px; top: 166px;
    font-size: 12px; color: var(--ink-soft);
  }
  .contact-lines {
    position: absolute; left: 30px; top: 186px;
    list-style: none; font-size: 12px; line-height: 15px; color: var(--ink-soft);
  }
  .contact-lines .label { color: var(--brand-blue); font-weight: 600; }
  .contact-lines .sep { color: var(--brand-blue); padding: 0 4px; }
  .website {
    font-size: 14px; font-weight: 600; letter-spacing: 3px;
    color: var(--brand-blue);
  }
  .card--front .website { position: absolute; left: 30px; top: 240px; }
  .brand-mark {
    position: absolute; right: 40px; top: 104px;
    width: 120px; height: 120px; border-radius: 8px;
    background: var(--brand-blue);
  }
  .back-center {
    position: absolute; inset: 0;
    display: flex; flex-direction: column; align-items: center;
  }
  .back-center .brand-name { margin-top: 104px; font-size: 36px; }
  .back-center .website { margin-top: auto; margin-bottom: 12px; }
  .card--back-blue .brand-name,
  .card--back-blue .website { color: var(--on-blue); }
</style>
</head>
<body>
  <section class="card card--front" aria-label="Business card front">
    <div class="brand-name">Brightfern Co</div>
    <div class="contact-name">Corisse Pallant</div>
    <div class="contact-title">Brand Manager</div>
    <div class="contact-address">4127 Dunford Avenue, Burnaby, B.C. V3K 8T2</div>
    <ul class="contact-lines">
      <li><span class="label">T :</span> 1-888-472-1950<span class="sep">|</span><span class="label">F :</span> 604-281-7734 ext. 120</li>
      <li><span class="label">C :</span> 604-519-2086<span class="sep">|</span><span class="label">F :</span> 604-281-7790</li>
      <li><span class="label">E :</span> corisse@brightfernco.ca</li>
    </ul>
    <div class="website">brightfernco.ca</div>
    <div class="brand-mark" aria-hidden="true"></div>
  </section>

  <section class="card card--back-light" aria-label="Business card back, light">
    <div class="back-center">
      <div class="brand-name">Brightfern Co</div>
      <div class="website">brightfernco.ca</div>
    </div>
  </section>

  <section class="card card--back-blue" aria-label="Business card back, blue">
    <div class="back-center">
      <div class="brand-name">Brightfern Co</div>
      <div class="website">brightfernco.ca</div>
    </div>
  </section>
</body>
</html>
```